Global Developmental Delay Awareness Day Poster

I need a poster to raise awareness for a condition called Global Developmental Delay (GDD) . The day of awareness for this condition is May 1. The condition is something found in children who are significantly delayed in their milestones. We are hopeful that through education and support more children with this condition can gain access to therapies and support to minimize the long term effects and maxamise their potential. Theme for GDD awareness is yellow so lots of yellow needed. Can be any yellow. Like it to be colourful, but not bright if that makes sense. I'd like it to be classy but fun and childish - this is a childhood diagnosis. Just not 'tacky'. Like the design to reflect the wonders of childhood so feel free to use your imagination!

Target Market(s)

Mums (and dads) of young children under 5

Colors
fee18a
fbf289

Requirements
Must have
• cheery, childish, happy feel - see uploaded poster examples for ideas. They are just ideas for theme. Different fun, childish fonts and 'sections' - perhaps with different colour backgrounds etc.
• Heading should be "Global Developmental Delay" or something similar
• Must have text as in the attachment
• Must have yellow 'theme'
• more colours than just yellow.
Nice to have
• colors - not bright but colorful.

```html
<!DOCTYPE html>
<html lang="en">
<head>
<meta charset="utf-8">
<title>Global Developmental Delay Awareness Poster</title>
<link rel="stylesheet" href="https://fonts.googleapis.com/css2?family=Fredoka:wght@500;600&family=Montserrat:wght@400;600;700&display=swap">
<style>
:root{
  --red:#e8202a;
  --yellow:#fbf289;
  --gold:#f6d889;
  --ink:#1d1d1d;
  --white:#ffffff;
  --stage:#efefec;
}
*{margin:0;padding:0;box-sizing:border-box}
html,body{width:1200px;height:1200px;overflow:hidden;background:var(--stage)}
.poster{
  position:absolute;left:173px;top:0;width:865px;height:1215px;
  transform:scale(.9877);transform-origin:top left;
  background:var(--white);overflow:hidden;
  font-family:'Montserrat',sans-serif;color:var(--ink);
}
.abs{position:absolute}
.band{left:0;top:0;width:865px;height:1215px}
.display{font-family:'Fredoka',sans-serif;font-weight:600}
.title{left:0;width:865px;text-align:center;color:var(--red);line-height:1}
.title-top{top:22px;font-size:98px}
.title-bottom{top:122px;font-size:74px}
.hero{left:560px;top:201px;width:396px;height:396px;border-radius:50%;border:3px solid var(--red);
  background:radial-gradient(circle at 45% 55%,#a9724a 0 22%,#f3c9a8 23% 40%,#fbf3d6 41%)}
.section-head{color:var(--red)}
.what-head{left:27px;top:248px;font-size:54px;line-height:1}
.intro{left:27px;top:318px;width:540px;font-size:15.5px;line-height:19px}
.checks{left:31px;top:394px;width:480px;display:grid;grid-template-columns:236px 220px;row-gap:14px;font-weight:700;font-size:16.5px}
.checks li{list-style:none;display:flex;align-items:center;gap:4px}
.checks svg{flex:none}
.do-card{left:46px;top:498px;width:327px;height:292px;background:var(--red);border-radius:8px;overflow:hidden;box-shadow:0 4px 6px rgba(0,0,0,.18)}
.do-art{height:96px;background:linear-gradient(#ffffff 0,#fde7d8 55%,var(--red))}
.do-head{color:var(--gold);font-size:25px;text-align:center;margin-top:2px;line-height:1.1}
.do-text{color:var(--white);font-size:15px;line-height:19px;text-align:center;padding:0 8px}
.pill{background:var(--red);border-radius:18px;text-align:center;line-height:1}
.concern-pill{left:62px;top:806px;width:264px;height:40px;color:var(--white);font-size:25px;padding-top:6px;border:2px solid #fff;box-shadow:0 0 0 1px var(--red)}
.concern-text{left:29px;top:860px;width:360px;font-size:13.6px;line-height:17px}
.cause-pill{left:420px;top:578px;width:240px;height:34px;color:var(--gold);font-size:24px;padding-top:5px}
.cause-text{left:428px;top:624px;width:420px;font-size:15px;line-height:19px}
.cause-text p+p{margin-top:14px}
.causes{margin-top:12px}
.causes li{list-style:none;font-weight:700;font-size:16px;height:34px;display:flex;align-items:center;gap:10px}
.causes li::before{content:"";width:5px;height:5px;border-radius:50%;background:var(--red)}
.contact-tab{left:68px;top:973px;width:184px;height:36px;background:var(--yellow);border-radius:14px 14px 0 0;font-weight:700;font-size:24px;text-align:center;padding-top:2px}
.contact-panel{left:0;top:1007px;width:324px;height:171px;background:var(--red);border-radius:0 14px 0 0;color:var(--white)}
.contact-row{position:absolute;left:36px;display:flex;align-items:center;gap:10px;font-size:13px;line-height:15px}
.contact-row.phone{top:18px;font-size:16px;font-weight:700}
.contact-row.addr{top:52px}
.contact-row.mail{top:92px}
.contact-row.web{top:116px}
.follow{position:absolute;left:78px;top:144px;font-size:13px;display:flex;align-items:center;gap:6px}
.follow span.dot{width:12px;height:12px;border-radius:50%;border:2px solid #fff}
.kids-art{left:330px;top:960px;width:510px;height:218px;background:radial-gradient(ellipse at 50% 60%,#f4b46a 0,#e39a58 40%,rgba(255,255,255,0) 72%)}
.foot{left:0;top:1178px;width:865px;height:37px;background:var(--yellow)}
</style>
</head>
<body>
<main class="poster">
  <svg class="abs band" viewBox="0 0 865 1215" aria-hidden="true">
    <path d="M0 213 Q430 250 865 212 L865 560 Q600 480 360 520 Q150 555 0 560 Z" fill="var(--yellow)"/>
  </svg>

  <h1 class="abs display title title-top">Global</h1>
  <div class="abs display title title-bottom">Developmental Delay</div>

  <div class="abs hero" role="img" aria-label="Illustration of two boys carrying a brown sack together"></div>

  <h2 class="abs display section-head what-head">What is GDD ?</h2>
  <p class="abs intro">A developmental delay is more than being ‘a little behind.” Global developmental delay (GDD)is diagnosed when a child is significantly delayed in two or more of the 5 developmental realms including</p>

  <ul class="abs checks">
    <li><svg width="18" height="16" viewBox="0 0 18 16"><rect x="1" y="3" width="12" height="12" fill="none" stroke="#e8202a" stroke-width="2"/><path d="M4 8l3 4 10-11" fill="none" stroke="#e8202a" stroke-width="2.4"/></svg>Cognitive (or thinking)</li>
    <li><svg width="18" height="16" viewBox="0 0 18 16"><rect x="1" y="3" width="12" height="12" fill="none" stroke="#e8202a" stroke-width="2"/><path d="M4 8l3 4 10-11" fill="none" stroke="#e8202a" stroke-width="2.4"/></svg>Social and emotional</li>
    <li><svg width="18" height="16" viewBox="0 0 18 16"><rect x="1" y="3" width="12" height="12" fill="none" stroke="#e8202a" stroke-width="2"/><path d="M4 8l3 4 10-11" fill="none" stroke="#e8202a" stroke-width="2.4"/></svg>Communication</li>
    <li><svg width="18" height="16" viewBox="0 0 18 16"><rect x="1" y="3" width="12" height="12" fill="none" stroke="#e8202a" stroke-width="2"/><path d="M4 8l3 4 10-11" fill="none" stroke="#e8202a" stroke-width="2.4"/></svg>&nbsp;Fine motor</li>
    <li><svg width="18" height="16" viewBox="0 0 18 16"><rect x="1" y="3" width="12" height="12" fill="none" stroke="#e8202a" stroke-width="2"/><path d="M4 8l3 4 10-11" fill="none" stroke="#e8202a" stroke-width="2.4"/></svg>Gross motor</li>
  </ul>

  <section class="abs do-card">
    <div class="do-art" role="img" aria-label="Illustration of five happy children jumping"></div>
    <h3 class="display do-head">What can you do?</h3>
    <p class="do-text">Each child is different in their own wonderful way, if we choose to celebrate and understand the things that make us unique as well as the ones that bring us together, we can create a much happier and more inclusive environment for all<br>our children.</p>
  </section>

  <h3 class="abs display pill concern-pill">If you are concerned</h3>
  <p class="abs concern-text">Early intervention programs and therapies can give many children with global development delays a head start and allow them to reach their full potential. If you are concerned that your child is not developing at the rate you would expect, please talk to your GP.</p>

  <h3 class="abs display pill cause-pill">What causes GDD</h3>
  <div class="abs cause-text">
    <p>There are many possible causes of GDD. Some are permanent, but others aren’t.</p>
    <p>They include</p>
    <ul class="causes">
      <li>Genetic conditions</li>
      <li>Complications in pregnancy or birth</li>
      <li>Environmental issues</li>
      <li>Other medical conditions</li>
    </ul>
    <p class="cause-note">More often than not a child received a secondary diagnosis as they grow such as intellectual disability or autism spectrum disorder, in which case the name for the disorder replaces the term developmental delay.</p>
  </div>

  <div class="abs kids-art" role="img" aria-label="Illustration of four cheerful children jumping with arms raised"></div>

  <div class="abs contact-tab">Contact us</div>
  <section class="abs contact-panel">
    <div class="contact-row phone"><svg width="24" height="24" viewBox="0 0 24 24"><circle cx="12" cy="12" r="11" fill="none" stroke="#f6d889" stroke-width="2"/><path d="M8 6l2 3-1 2c1 2 2 3 4 4l2-1 3 2-1 2c-5 0-10-5-10-10z" fill="#f6d889"/></svg>020 7946 0321</div>
    <div class="contact-row addr"><svg width="16" height="20" viewBox="0 0 16 20"><path d="M8 1a7 7 0 0 0-7 7c0 5 7 11 7 11s7-6 7-11a7 7 0 0 0-7-7z" fill="#f6d889"/><circle cx="8" cy="8" r="3" fill="#e8202a"/></svg>Lorem ipsum dolor sit amet,<br>consectetur adipiscing elit,</div>
    <div class="contact-row mail"><svg width="18" height="13" viewBox="0 0 18 13"><rect width="18" height="13" fill="#f6d889"/><path d="M0 0l9 7 9-7" fill="none" stroke="#e8202a" stroke-width="1.5"/></svg>hello@brightsteps.org</div>
    <div class="contact-row web"><svg width="16" height="16" viewBox="0 0 16 16" fill="none" stroke="#f6d889" stroke-width="1.4"><circle cx="8" cy="8" r="7"/><ellipse cx="8" cy="8" rx="3" ry="7"/><path d="M1 8h14M2 4.5h12M2 11.5h12"/></svg>www.brightsteps.org</div>
    <div class="follow">Follow us @ <span class="dot"></span> brightsteps</div>
  </section>

  <div class="abs foot"></div>
</main>
</body>
</html>
```